Software static HTML page design

We need 5 static HTML pages designed for our current software startup - TallyNest. All details are attached in a document for consideration.

Target Market(s)

Sporting clubs/University clubs

Industry/Entity Type

Software

Number of Pages Required

5+ page

Font styles to use
Sans Serif

Colors
33a6d7
85cae6
86cfc6
33b8a4
ffffff

```html
<!DOCTYPE html>
<html lang="en">
<head>
<meta charset="utf-8">
<title>TallyNest — Pricing</title>
<link href="https://fonts.googleapis.com/css2?family=Raleway:wght@400;500;600;700&family=Open+Sans:wght@400;600&display=swap" rel="stylesheet">
<style>
:root{
  --blue:#33a6d7;
  --sky:#85cae6;
  --mint:#86cfc6;
  --teal:#33b8a4;
  --white:#ffffff;
  --navy:#3e6e96;
  --navy-line:#5a87aa;
  --ink:#2f3438;
  --body:#5b6166;
  --muted:#9aa1a6;
  --mist:#f3f7f9;
  --rule:#e4e8eb;
  --band1:#2fb09e;
  --band2:#3dbbaa;
  --band3:#52c2b2;
  --band4:#68c8bb;
  --band5:#86cfc6;
}
*{box-sizing:border-box;margin:0;padding:0}
html,body{width:1200px;height:3830px;overflow:hidden}
body{position:relative;background:var(--white);font-family:"Open Sans",sans-serif;color:var(--body);font-size:12px;line-height:1.75}
.abs{position:absolute}
h1,h2,h3,.label,.brand,.nav a,.btn{font-family:"Raleway",sans-serif}

/* hero */
.hero-bg{left:0;top:0;width:1200px;height:720px;background:linear-gradient(100deg,var(--blue) 0%,#35b2c0 55%,var(--teal) 100%);clip-path:polygon(0 0,100% 0,100% 720px,0 600px)}
.brand{left:161px;top:26px;display:flex;align-items:center;gap:10px;color:var(--white);font-weight:700;font-size:22px;letter-spacing:1px}
.brand .mark{width:22px;height:22px;background:var(--white)}
.nav{left:490px;top:30px;display:flex;gap:0}
.nav a{color:var(--white);text-decoration:none;font-size:12px;font-weight:600;letter-spacing:1px;margin-right:48px}
.nav-btn{top:26px;height:30px;border:1.5px solid var(--white);color:var(--white);font-family:"Raleway",sans-serif;font-size:12px;font-weight:600;letter-spacing:1px;display:flex;align-items:center;justify-content:center}
.hero-title{left:0;width:1200px;text-align:center;color:var(--white);font-weight:400;letter-spacing:2px}
.hero-title.small{top:132px;font-size:24px}
.hero-title.large{top:174px;font-size:30px;letter-spacing:3px}
.hero-title b{font-weight:700}

/* plan cards */
.card-payg{left:161px;top:270px;width:470px;height:407px;background:var(--white);box-shadow:0 6px 24px rgba(0,0,0,.12)}
.card-title{position:absolute;left:0;width:100%;text-align:center;font-size:16px;font-weight:700;letter-spacing:1.5px}
.card-payg .card-title{top:28px;color:var(--teal)}
.rate{position:absolute;top:90px;width:200px;text-align:center}
.rate .num{font-family:"Raleway",sans-serif;color:var(--teal);font-size:24px;font-weight:700}
.rate .num small{font-size:15px;font-weight:500}
.rate .note{font-size:11px;color:var(--muted);line-height:1.2}
.perks{position:absolute;left:105px;top:192px;list-style:none}
.perks li{display:flex;align-items:center;gap:14px;height:37px;font-size:12px;color:var(--body)}
.perks .dot{width:24px;height:24px;border-radius:50%;background:#e3f4f1;display:flex;align-items:center;justify-content:center}
.perks .dot i{width:8px;height:8px;border-radius:50%;background:var(--teal)}
.card-foot{position:absolute;left:0;bottom:0;width:100%;height:64px;background:var(--mist);border-top:1px solid var(--rule);display:flex;align-items:center;justify-content:center;font-family:"Raleway",sans-serif;color:var(--teal);font-size:12px;font-weight:600;letter-spacing:1.5px}
.card-ent{left:631px;top:301px;width:408px;height:324px;background:var(--navy);color:var(--white)}
.card-ent .card-title{top:24px;color:var(--white)}
.card-ent .desc{position:absolute;left:50px;top:78px;width:310px;text-align:center;font-size:13px;color:#b9d0e2;line-height:1.7}
.ent-grid{position:absolute;left:38px;top:152px;display:grid;grid-template-columns:143px 174px;gap:0 10px}
.ent-grid span{height:46px;display:flex;align-items:center;justify-content:center;font-size:12px;color:var(--white);border-bottom:1px solid var(--navy-line)}
.ent-grid span:nth-child(odd){border-right:1px solid var(--navy-line)}
.card-ent .foot{position:absolute;left:0;bottom:0;width:100%;height:52px;border-top:1px solid var(--navy-line);display:flex;align-items:center;justify-content:center;font-family:"Raleway",sans-serif;font-size:12px;letter-spacing:1.5px;color:#c3d6e5}

/* payments */
.section-head{left:0;width:1200px;text-align:center}
.section-head h2{font-size:24px;font-weight:500;color:var(--teal)}
.section-head p{font-size:16px;color:var(--ink);margin-top:2px}
.rule{left:161px;width:878px;height:1px;background:var(--rule)}
.row-label{font-size:22px;font-weight:500;color:var(--ink);line-height:1.3}
.row-text{width:400px;font-size:11.5px;color:var(--body);line-height:1.85}
.row-text a{color:var(--blue);text-decoration:none}
.vrule{width:1px;background:var(--rule)}
.price-col{width:200px;text-align:center}
.price-col .num{font-family:"Raleway",sans-serif;font-size:22px;color:var(--teal);font-weight:500;line-height:1.2}
.price-col .note{font-size:11px;color:var(--muted);margin-bottom:20px}
.card-chip{display:inline-block;width:40px;height:18px;border-radius:3px;background:#d3d8dc;margin-right:16px}

/* also included */
.mist-bg{left:0;top:1100px;width:1200px;height:480px;background:var(--mist);clip-path:polygon(0 0,100% 60px,100% 400px,0 470px)}
.illus{border-radius:50%}
h3.block-title{font-size:20px;font-weight:600;color:var(--ink)}
.feature-list{list-style:none;display:grid;grid-template-columns:176px 181px 150px;row-gap:10px}
.feature-list li{font-size:11.5px;color:var(--body);display:flex;align-items:center;gap:8px;line-height:1.6}
.feature-list li::before{content:"";width:6px;height:6px;border-radius:50%;background:var(--teal)}

/* service bands */
.band{left:0;width:1200px;height:179px}
.band .icon{position:absolute;left:161px;top:68px;width:44px;height:44px;border-radius:50%;border:2px solid var(--white);display:flex;align-items:center;justify-content:center}
.band .icon i{width:14px;height:14px;border:2px solid var(--white);border-radius:3px}
.band .label{position:absolute;left:222px;top:74px;font-size:21px;color:var(--white);font-weight:500}
.band .row-text{position:absolute;left:391px;top:50px;color:#e9f7f5}
.band .row-text a{color:var(--ink)}
.band .vrule{position:absolute;left:853px;top:50px;height:80px;background:rgba(255,255,255,.35)}
.band .price{position:absolute;left:908px;top:74px;font-size:21px;color:var(--ink);font-family:"Raleway",sans-serif;font-weight:500}

/* faq */
.faq{width:440px}
.faq h4{display:flex;align-items:center;gap:12px;font-family:"Raleway",sans-serif;font-size:17px;font-weight:600;color:var(--teal)}
.faq h4 .q{width:30px;height:30px;border-radius:50%;background:var(--teal);color:var(--white);font-size:16px;display:flex;align-items:center;justify-content:center}
.faq p{margin-top:14px;font-size:11.5px;color:var(--ink);line-height:1.9}

/* cta + footer */
.cta-bg{left:0;top:3260px;width:1200px;height:570px;background:linear-gradient(180deg,#ffffff 0%,#f2f5f7 30%,#eef2f5 100%)}
.cta-title{left:161px;top:3390px;font-family:"Raleway",sans-serif;font-size:22px;color:var(--teal)}
.cta-sub{left:161px;top:3428px;font-size:16px;color:var(--ink)}
.btn{top:3426px;height:36px;display:flex;align-items:center;justify-content:center;font-size:12px;font-weight:600;letter-spacing:1.5px}
.btn.outline{left:751px;width:148px;border:1.5px solid var(--teal);color:var(--teal);background:var(--white)}
.btn.solid{left:909px;width:128px;background:var(--teal);color:var(--white)}
.foot-rule{left:0;top:3503px;width:1200px;height:1px;background:#e1e6ea}
.foot-brand{left:161px;top:3550px;display:flex;align-items:center;gap:10px;font-family:"Raleway",sans-serif;font-weight:700;font-size:22px;color:#c9cfd4;letter-spacing:1px}
.foot-brand .mark{width:22px;height:22px;background:#c9cfd4}
.foot-desc{left:161px;top:3618px;width:200px;font-size:11px;color:var(--body);line-height:1.7}
.socials{left:161px;top:3698px;display:flex;gap:8px}
.socials i{width:14px;height:14px;background:#b7bfc5;border-radius:2px}
.foot-col{top:3540px}
.foot-col h5{font-family:"Raleway",sans-serif;font-size:12px;font-weight:700;letter-spacing:1.5px;color:var(--ink);margin-bottom:20px}
.foot-col a{display:block;font-size:11px;color:var(--body);text-decoration:none;line-height:20px}
.copyright{left:0;top:3782px;width:1200px;text-align:center;font-size:10px;color:var(--body);letter-spacing:.5px}
</style>
</head>
<body>

<!-- hero -->
<div class="abs hero-bg"></div>
<div class="abs brand"><span class="mark"></span>TallyNest</div>
<nav class="abs nav"><a href="#">HOME</a><a href="#">FEATURES</a><a href="#">PRICING</a><a href="#">CONTACT</a></nav>
<div class="abs nav-btn" style="left:886px;width:69px">LOGIN</div>
<div class="abs nav-btn" style="left:965px;width:66px">SIGNUP</div>
<h1 class="abs hero-title small">SIMPLE, TRANSPARENT PRICING.</h1>
<h1 class="abs hero-title large">ALWAYS KNOW WHAT <b>YOU'LL PAY</b></h1>

<section class="abs card-payg">
  <h2 class="card-title">PAY AS YOU GO</h2>
  <div class="rate" style="left:32px"><div class="num">1.75% <small>+ 30¢</small></div><div class="note">for domestic cards</div></div>
  <div class="rate" style="left:236px"><div class="num">2.9% <small>+ 30¢</small></div><div class="note">for International cards</div></div>
  <ul class="perks">
    <li><span class="dot"><i></i></span>No setup, monthly, or hidden fees</li>
    <li><span class="dot"><i></i></span>Pay as you go, only for what you use</li>
    <li><span class="dot"><i></i></span>Real-time fee reporting</li>
  </ul>
  <div class="card-foot">CREATE ACCOUNT &rarr;</div>
</section>

<section class="abs card-ent">
  <h2 class="card-title">ENTERPRISE</h2>
  <p class="desc">Tillway offers everything needed to run an online business at scale. Get in touch for details.</p>
  <div class="ent-grid">
    <span>Account management</span><span>Volume discounts</span>
    <span>Migration assistance</span><span>Dedicated support</span>
  </div>
  <div class="foot">CONTACT SALES &rarr;</div>
</section>

<!-- payments -->
<div class="abs section-head" style="top:732px"><h2>Payments</h2><p>Neuorrouisuam estui dolorem isum.</p></div>
<div class="abs rule" style="top:832px"></div>

<svg class="abs" style="left:161px;top:930px" width="52" height="40" viewBox="0 0 52 40" aria-hidden="true">
  <rect x="10" y="2" width="40" height="26" rx="3" fill="#b8c2cc"/>
  <rect x="2" y="10" width="40" height="26" rx="3" fill="#8e9bab"/>
  <rect x="2" y="16" width="40" height="5" fill="#6d7b8b"/>
</svg>
<div class="abs row-label" style="left:243px;top:925px">Credit &amp;<br>debit cards</div>
<p class="abs row-text" style="left:391px;top:880px">At vero eos et accusamus et iusto odio dignissimos ducimus qui blanditi praesentium voluptatum deleniti atque corrupti quos dolores et quasmo estias excepturi sint occaecati cupiditate non provsamus et iusto odio dignissimos ducimus qui blanditiisraesentium voluptatum deleniti atque corrupti quos dolore et quasmo edignissimos ducimus qui blanditiisrae sentium voluptatum deleniti atquestias exstias excer. <a href="#">Read More</a></p>
<div class="abs" style="left:391px;top:1040px"><span class="card-chip"></span><span class="card-chip"></span><span class="card-chip"></span></div>
<div class="abs vrule" style="left:853px;top:880px;height:140px"></div>
<div class="abs price-col" style="left:880px;top:885px">
  <div class="num">1.75% + 30¢</div><div class="note">for domestic cards</div>
  <div class="num">2.9% + 30¢</div><div class="note">for International cards</div>
</div>

<!-- also included -->
<div class="abs mist-bg"></div>
<div class="abs illus" role="img" aria-label="Illustration of a hand holding a payment card" style="left:205px;top:1277px;width:127px;height:115px;background:radial-gradient(circle at 50% 50%,#3aa98a 0%,#86cfc6 60%,#dfeeed 100%)"></div>
<h3 class="abs block-title" style="left:391px;top:1208px">Also included</h3>
<p class="abs row-text" style="left:391px;top:1265px;width:560px">At vero eos et accusamus et iusto odio dignissimos ducimus qui blanditiisraesentium volu orrupti quos dolores et quasmo estias excepturi sint occaecati cupiditate non prov.</p>
<ul class="abs feature-list" style="left:391px;top:1348px">
  <li>Smarter saved cards</li><li>Full data portability</li><li>Wallet Pay</li>
  <li>Simple PCI compliance</li><li>Accounting integrations</li><li>Mobile Dashboard</li>
  <li>Integrated fraud tools</li><li>Team security controls</li><li>Webhooks</li>
</ul>
<p class="abs row-text" style="left:391px;top:1466px;width:560px">We'll automatically convert payments accepted in other currencies. <a href="#">Learn more</a></p>

<!-- disputes -->
<div class="abs illus" role="img" aria-label="Illustration of interlocking gears" style="left:215px;top:1670px;width:106px;height:92px;background:radial-gradient(circle at 40% 45%,#3aa0c9 0%,#5b6f80 55%,#ffffff 80%)"></div>
<h3 class="abs block-title" style="left:391px;top:1648px">Disputes</h3>
<p class="abs row-text" style="left:391px;top:1705px">At vero eos et accusamus et iusto odio dignissimos ducimus qui blanditi praesentium voluptatum deleniti atque corrupti quos dolores et quasmo estias excepturi sint occaecati cupiditate non prov. <a href="#">Read More</a></p>
<div class="abs vrule" style="left:853px;top:1700px;height:80px"></div>
<div class="abs" style="left:883px;top:1729px;font-family:'Raleway',sans-serif;font-size:20px;color:var(--teal)">A$25.00 or A$0</div>

<!-- service bands -->
<svg class="abs" style="left:0;top:1850px" width="1200" height="104" viewBox="0 0 1200 104" aria-hidden="true">
  <polygon points="0,50 380,8 1200,85 1200,104 0,104" fill="#2fb09e"/>
</svg>
<section class="abs band" style="top:1953px;background:var(--band1)">
  <span class="icon"><i></i></span><span class="label">Subscriptions</span>
  <p class="row-text">At vero eos et accusamus et iusto odio dignissimos ducimus qui blanditi praesentium voluptatum deleniti atque corrupti quos dolores et quasmo estias excepturi sint occaecati cupiditate non prov. <a href="#">Read More</a></p>
  <span class="vrule"></span><span class="price">Included</span>
</section>
<section class="abs band" style="top:2132px;background:var(--band2)">
  <span class="icon"><i></i></span><span class="label">Connect</span>
  <p class="row-text">At vero eos et accusamus et iusto odio dignissimos ducimus qui blanditi praesentium voluptatum deleniti atque corrupti quos dolores et quasmo estias excepturi sint occaecati cupiditate non prov. <a href="#">Read More</a></p>
  <span class="vrule"></span><span class="price">Included</span>
</section>
<section class="abs band" style="top:2311px;background:var(--band3)">
  <span class="icon"><i></i></span><span class="label">Courier</span>
  <p class="row-text">At vero eos et accusamus et iusto odio dignissimos ducimus qui blanditi praesentium voluptatum deleniti atque corrupti quos dolores et quasmo estias excepturi sint occaecati cupiditate non prov. <a href="#">Read More</a></p>
  <span class="vrule"></span><span class="price">Up to 0.5%</span>
</section>
<section class="abs band" style="top:2490px;background:var(--band4)">
  <span class="icon"><i></i></span><span class="label">Harbor</span>
  <p class="row-text">At vero eos et accusamus et iusto odio dignissimos ducimus qui blanditi praesentium voluptatum deleniti atque corrupti quos dolores et quasmo estias excepturi sint occaecati cupiditate non prov. <a href="#">Read More</a></p>
  <span class="vrule"></span><span class="price">USD $500</span>
</section>
<section class="abs band" style="top:2669px;background:var(--band5)">
  <span class="icon"><i></i></span><span class="label">Watchtower</span>
  <p class="row-text">At vero eos et accusamus et iusto odio dignissimos ducimus qui blanditi praesentium voluptatum deleniti atque corrupti quos dolores et quasmo estias excepturi sint occaecati cupiditate non prov. <a href="#">Read More</a></p>
  <span class="vrule"></span><span class="price">Included</span>
</section>
<svg class="abs" style="left:0;top:2847px" width="1200" height="130" viewBox="0 0 1200 130" aria-hidden="true">
  <polygon points="0,0 1200,0 1200,45 0,125" fill="#86cfc6"/>
</svg>

<!-- faq -->
<div class="abs faq" style="left:161px;top:2966px">
  <h4><span class="q">?</span>Sed ut perspicomnilstatu?</h4>
  <p>At vero eos et accusamus et iusto odio dignissimos ducimus qui blanditi sraesentium voluptatum deleniti atque corrupti quos dolor.</p>
</div>
<div class="abs faq" style="left:638px;top:2966px">
  <h4><span class="q">?</span>Sed ut perspicomnilstatu?</h4>
  <p>At vero eos et accusamus et iusto odio dignissimos ducimus qui blanditi sraesentium voluptatum deleniti atque corrupti quos dolort vero eos et accusamus et iusto odio dignissimos ducimus qui blanditiisraesentium voluptatum deleniti atque corrupti quos dolor.</p>
</div>
<div class="abs faq" style="left:161px;top:3109px">
  <h4><span class="q">?</span>Sed ut perspiciatis unde omnilstatu?</h4>
  <p>At vero eos et accusamus et iusto odio dignissimos ducimus qui blanditi sraesentium voluptatum deleniti atque corrupti.</p>
</div>

<!-- call to action -->
<div class="abs cta-bg"></div>
<div class="abs cta-title">Ready to get started?</div>
<div class="abs cta-sub">Get in touch, or create an account.</div>
<div class="abs btn outline">CREATE ACCOUNT</div>
<div class="abs btn solid">CONTACT US</div>

<!-- footer -->
<div class="abs foot-rule"></div>
<div class="abs foot-brand"><span class="mark"></span>TallyNest</div>
<p class="abs foot-desc">Sed ut perspiciatis unde omnis iste natus error sit voluptatem accusantium doloremque laudantium</p>
<div class="abs socials"><i></i><i></i><i></i><i></i><i></i></div>
<div class="abs foot-col" style="left:434px"><h5>PRODUCTS</h5><a href="#">Payments</a><a href="#">Subscriptions</a><a href="#">Connect</a><a href="#">Courier</a><a href="#">Pricing</a><a href="#">Works with Us</a><a href="#">Global</a></div>
<div class="abs foot-col" style="left:592px"><h5>DEVELOPERS</h5><a href="#">Documentation</a><a href="#">API reference</a><a href="#">API status</a><a href="#">Open source</a></div>
<div class="abs foot-col" style="left:786px"><h5>COMPANY</h5><a href="#">About</a><a href="#">Customers</a><a href="#">Jobs</a><a href="#">Blog</a><a href="#">Press</a></div>
<div class="abs foot-col" style="left:945px"><h5>RESOURCES</h5><a href="#">Support</a><a href="#">Contact</a><a href="#">Privacy &amp; terms</a></div>
<div class="abs copyright">© 2017 TALLYNEST. ALL RIGHTS RESERVED. PRIVACY POLICY. TERMS AND CONDITIONS</div>

</body>
</html>
```